Business card for Industrial Automation Company.

The company is called Process and Signal Dynamics. We are a systems integration company in South Africa specializing in PLC and SCADA programming, systems integration and industrial automation. Attached find logo and cover letter of the company for a feel of the general look. The website is still under development, so you will have to use your own ideas.

Please blend the colors on the business card as per the logo colors. Must be clean, professional look. Please submit a creative professional design. If a background color is used please do not use dark colored backgrounds.

Target Market(s)

Mining

Industry/Entity Type

Engineering Consultant

Contact Information for Business Card

Gerrit van Dyk (NDip Instrumentation; BEng)
Director / Systems Engineer

Postal Address
PO Box 2867
Vredenburg
7380

Physical Address:
Kloofhoek Street 27
Vredenburg
7380

Tel: +22 548 6170
Cell: +27 82 953 4086
Mail: gerritv@psd-zx.com
Web: www.psd-zx.com

Font styles to use
Sans Serif

Colors

Designer to choose colors to be used in the design.

Requirements
Must have
• Backside of the card must also contain the following:
• Services
• *Industrial Automation
• *Control System design and configuration
• *Systems Integration
• *Equipment Supply
• Industries
• *Mining
• *Factory
• *Oil and Gas
Nice to have
• Colors must blend in with colors of logo. Not too much color and no dark backgrounds.
Should not have
• dark / black background. Preferably white / light background if any.

```html
<!DOCTYPE html>
<html lang="en">
<head>
<meta charset="utf-8">
<title>Process and Signal Dynamics – Business Card</title>
<link href="https://fonts.googleapis.com/css2?family=Arimo:wght@400;700&display=swap" rel="stylesheet">
<style>
  :root{
    --navy:#1d3f87;
    --lime:#c8d72a;
    --grey:#5f6368;
    --grey-stripe:#6d6f73;
    --tint:#eceef4;
    --paper:#ffffff;
    --stage:#e9eaed;
  }
  *{box-sizing:border-box;margin:0;padding:0}
  html,body{width:1200px;height:880px;overflow:hidden}
  body{background:var(--stage);font-family:"Arimo",Arial,sans-serif;color:var(--grey);position:relative}
  .card{position:absolute;left:250px;width:700px;height:400px;background:var(--paper);border-radius:22px;overflow:hidden;box-shadow:0 6px 18px rgba(0,0,0,.12)}
  .card--back{top:20px}
  .card--front{top:460px}

  /* brand block */
  .brand{position:absolute}
  .brand__row{display:flex;align-items:center;gap:12px}
  .brand__dot{width:30px;height:30px;border-radius:50%;background:var(--navy)}
  .brand__name{font-weight:700;color:var(--navy);font-size:30px;letter-spacing:-.3px;line-height:1}
  .brand__tagline{font-size:14px;letter-spacing:1.6px;color:var(--grey);margin-top:8px}

  /* back */
  .back__tint{position:absolute;left:0;top:150px;width:300px;height:250px;background:radial-gradient(ellipse at 40% 55%,#e3e5ee 0%,var(--tint) 45%,rgba(236,238,244,0) 75%)}
  .card--back .brand{left:240px;top:50px}
  .offer{position:absolute;left:270px;top:140px}
  .offer__heading{font-weight:700;color:var(--navy);font-size:17px;margin-bottom:6px}
  .offer__list{list-style:none;margin-bottom:16px}
  .offer__list li{font-size:16px;color:var(--grey);line-height:22px;padding-left:20px;position:relative}
  .offer__list li::before{content:"";position:absolute;left:4px;top:8px;width:7px;height:7px;border-radius:50%;background:var(--lime)}
  .back__web{position:absolute;right:40px;bottom:44px;font-size:16px;font-weight:700;color:var(--navy)}

  /* front */
  .card--front .brand{left:40px;top:40px}
  .person{position:absolute;left:40px;top:160px}
  .person__name{font-weight:700;color:var(--navy);font-size:27px}
  .person__quals{font-size:15px}
  .person__role{font-size:19px;color:var(--grey);margin-top:2px}
  .contact{position:absolute;left:60px;top:250px;font-size:18px;line-height:25px;color:var(--grey)}
  .contact b{color:var(--navy)}
  .front__accent{position:absolute;left:-22px;top:225px;width:44px;height:44px;border-radius:50%;background:var(--lime)}
  .rule-h{position:absolute;left:330px;top:135px;width:360px;height:1.5px;background:var(--lime)}
  .rule-v{position:absolute;width:1.5px;height:70px;background:var(--lime)}
  .rule-v--a{left:332px;top:205px}
  .rule-v--b{left:512px;top:150px}
  .address{position:absolute;font-size:17px;line-height:23px;color:var(--grey)}
  .address__label{font-weight:700;color:var(--navy);font-size:17px;margin-bottom:4px}
  .address--postal{left:350px;top:200px}
  .address--physical{left:530px;top:145px}
  .band{position:absolute;left:0;bottom:0;width:700px;height:80px}
  .front__web{position:absolute;right:36px;bottom:20px;font-size:17px;color:#fff}
</style>
</head>
<body>

<section class="card card--back" aria-label="Card back">
  <div class="back__tint" role="img" aria-label="Faint light decorative area"></div>
  <div class="brand">
    <div class="brand__row"><span class="brand__name">Process and Signal Dynamics</span></div>
    <div class="brand__tagline">Engineering reliable control systems!</div>
  </div>
  <div class="offer">
    <h2 class="offer__heading">SERVICES</h2>
    <ul class="offer__list">
      <li>Industrial Automation</li>
      <li>Control System design and configuration</li>
      <li>Systems Integration</li>
      <li>Equipment Supply</li>
    </ul>
    <h2 class="offer__heading">INDUSTRIES</h2>
    <ul class="offer__list">
      <li>Mining</li>
      <li>Factory</li>
      <li>Oil and Gas</li>
    </ul>
  </div>
  <div class="back__web">www.psd-zx.com</div>
</section>

<section class="card card--front" aria-label="Card front">
  <div class="brand">
    <div class="brand__row"><span class="brand__dot"></span><span class="brand__name">Process and Signal Dynamics</span></div>
    <div class="brand__tagline">Engineering reliable control systems!</div>
  </div>

  <div class="front__accent"></div>
  <div class="person">
    <div class="person__name">Gerrit van Dyk <span class="person__quals">(NDip Instrumentation; BEng)</span></div>
    <div class="person__role">Director / Systems Engineer</div>
  </div>
  <div class="contact">
    <div><b>Tel:</b> +22 548 6170</div>
    <div><b>Cell:</b> +27 82 953 4086</div>
    <div><b>Mail:</b> gerritv@psd-zx.com</div>
  </div>

  <div class="rule-h"></div>
  <div class="rule-v rule-v--a"></div>
  <div class="rule-v rule-v--b"></div>
  <div class="address address--postal">
    <div class="address__label">Postal Address:</div>
    <div>PO Box 2867</div>
    <div>Kliprivierdal, 7412</div>
  </div>
  <div class="address address--physical">
    <div class="address__label">Physical Address:</div>
    <div>Kloofhoek Street 27</div>
    <div>Kliprivierdal, 7412</div>
  </div>

  <svg class="band" viewBox="0 0 700 80" aria-hidden="true">
    <path d="M0 64 L440 64 L462 34 L700 34 L700 80 L0 80 Z" fill="var(--navy)"/>
    <path d="M0 52 L432 52 L455 22 L466 22 L443 58 L0 58 Z" fill="var(--grey-stripe)"/>
  </svg>
  <div class="front__web">www.psd-zx.com</div>
</section>

</body>
</html>
```